Stanbrook Fire Services Pty Ltd

We need business cards for a company based in Perth, we install, service and maintain fire equipment.
On the front we want a great design with our logo and a small spot for our full company name, general company email address and office number. On the back we need space for our name, title, mobile number and email address on the back.

Target Market(s)

Facility managers and commercial/industrial building owners/occupiers.

Contact Information for Business Card

Font styles to use
Sans Serif

Requirements
Must have
• Please only submit 5 of your best samples.
Darker tones are preferred.
Nice to have
• We want to use, black, red and grey. Keep it modern and clean.
I've attached the company logo and a sample of a boarder we use on our emergency plans.
Should not have
• No preference. Let the designer choose.

```html
<!DOCTYPE html>
<html lang="en">
<head>
<meta charset="utf-8">
<title>Stanbrook Fire Services – Business Cards</title>
<link href="https://fonts.googleapis.com/css2?family=Montserrat:wght@300;400;700;800&family=Oswald:wght@500&display=swap" rel="stylesheet">
<style>
  :root {
    --bg: #161616;
    --card: #0c0c0c;
    --card-edge: #1e1e1e;
    --red: #e0242b;
    --white: #f4f4f4;
    --grey: #b9b9b9;
    --rule: #3a3a3a;
  }
  * { margin: 0; padding: 0; box-sizing: border-box; }
  html, body {
    width: 1200px; height: 900px; overflow: hidden;
    background: radial-gradient(ellipse at 50% 40%, #262626 0%, var(--bg) 70%);
    font-family: "Montserrat", Arial, sans-serif;
  }
  .canvas { position: relative; width: 1200px; height: 900px; }
  .card {
    position: absolute; left: 280px; width: 640px; height: 366px;
    background: linear-gradient(160deg, #151515 0%, var(--card) 60%);
    border: 1px solid var(--card-edge);
    border-radius: 26px; overflow: hidden;
    box-shadow: 0 18px 40px rgba(0,0,0,.55);
  }
  .card--front { top: 60px; }
  .card--back { top: 474px; }

  .wordmark {
    position: absolute; color: var(--red);
    font-family: "Montserrat", Arial, sans-serif; font-weight: 800;
    letter-spacing: 1px; line-height: 1; white-space: nowrap;
  }

  /* Front */
  .card--front .wordmark { left: 44px; top: 96px; font-size: 42px; }
  .front-band {
    position: absolute; left: 44px; right: 0; top: 168px; height: 9px;
    background: var(--red);
  }
  .company-name {
    position: absolute; left: 396px; top: 74px;
    color: var(--white); font-size: 20px; line-height: 1.12; text-transform: uppercase;
    white-space: nowrap;
  }
  .company-name__lead { display: block; font-weight: 700; letter-spacing: 1px; }
  .company-name__rest { display: block; font-weight: 300; letter-spacing: .5px; }

  .contact {
    position: absolute; display: flex; align-items: center; gap: 10px;
    color: var(--grey); font-size: 15px; font-weight: 400; letter-spacing: .5px;
    white-space: nowrap;
  }
  .contact svg { width: 14px; height: 14px; flex: none; }
  .card--front .contact--phone { left: 44px; top: 212px; }
  .card--front .contact--email { left: 250px; top: 272px; }

  /* Back */
  .card--back .wordmark { left: 48px; top: 164px; font-size: 32px; }
  .back-divider {
    position: absolute; left: 310px; top: 100px; width: 1px; height: 160px;
    background: var(--rule);
  }
  .person { position: absolute; left: 345px; top: 110px; }
  .person__name {
    font-family: "Oswald", Arial, sans-serif; font-weight: 500;
    color: var(--white); font-size: 26px; text-transform: uppercase; letter-spacing: .5px; line-height: 1.1;
  }
  .person__title {
    font-family: "Oswald", Arial, sans-serif; font-weight: 500;
    color: var(--red); font-size: 15px; text-transform: uppercase; letter-spacing: .5px;
  }
  .person__rule { width: 60px; height: 1px; background: var(--red); margin: 12px 0 14px; }
  .card--back .contact { position: static; margin-bottom: 10px; font-size: 14px; }
</style>
</head>
<body>
<main class="canvas">

  <section class="card card--front" aria-label="Business card front">
    <div class="wordmark">STANBROOK</div>
    <div class="company-name">
      <span class="company-name__lead">Stanbrook</span>
      <span class="company-name__rest">Fire Services</span>
      <span class="company-name__rest">Pty Ltd</span>
    </div>
    <div class="front-band"></div>
    <div class="contact contact--phone">
      <svg viewBox="0 0 24 24"><path fill="#e0242b" d="M6.6 10.8a15.1 15.1 0 0 0 6.6 6.6l2.2-2.2a1 1 0 0 1 1-.25 11.4 11.4 0 0 0 3.6.57 1 1 0 0 1 1 1V20a1 1 0 0 1-1 1A17 17 0 0 1 3 4a1 1 0 0 1 1-1h3.5a1 1 0 0 1 1 1c0 1.25.2 2.45.57 3.6a1 1 0 0 1-.25 1z"/></svg>
      <span>000 000 0000</span>
    </div>
    <div class="contact contact--email">
      <svg viewBox="0 0 24 24"><path fill="#e0242b" d="M2 5h20v14H2z"/><path fill="none" stroke="#0c0c0c" stroke-width="2" d="M2 5l10 8 10-8"/></svg>
      <span>office@stanbrookfire.com.au</span>
    </div>
  </section>

  <section class="card card--back" aria-label="Business card back">
    <div class="wordmark">STANBROOK</div>
    <div class="back-divider"></div>
    <div class="person">
      <div class="person__name">Your Name</div>
      <div class="person__title">Job Title</div>
      <div class="person__rule"></div>
      <div class="contact">
        <svg viewBox="0 0 24 24"><path fill="#e0242b" d="M6.6 10.8a15.1 15.1 0 0 0 6.6 6.6l2.2-2.2a1 1 0 0 1 1-.25 11.4 11.4 0 0 0 3.6.57 1 1 0 0 1 1 1V20a1 1 0 0 1-1 1A17 17 0 0 1 3 4a1 1 0 0 1 1-1h3.5a1 1 0 0 1 1 1c0 1.25.2 2.45.57 3.6a1 1 0 0 1-.25 1z"/></svg>
        <span>000 000 0000</span>
      </div>
      <div class="contact">
        <svg viewBox="0 0 24 24"><path fill="#e0242b" d="M2 5h20v14H2z"/><path fill="none" stroke="#0c0c0c" stroke-width="2" d="M2 5l10 8 10-8"/></svg>
        <span>name@stanbrookfire.com.au</span>
      </div>
    </div>
  </section>

</main>
</body>
</html>
```